Design a logo, banners, icons, etc for Wedding Planning Website

We are looking for a designer who can help design our new Wordpress wedding website/blog. The company is called Coral Dunes Luxury Weddings ([login to view URL]) We want something that suggests vintage but is also very light and feminine in terms of colours: gold, blush and mint are our favourites. But we also like black and white. It is important the designs are simple, clean and elegant - not fussy. We do not want the design to distract our potential clients from our images.

With regard to the logo, the emphasis should be on Luxury Weddings not so much Riviera Maya. We want something that works well for our social media profile images as well. Here are some ideas of sites we like:

We like our template, which is a Pemvora template but we need someone to help with the design of the blog, which include: • Custom Blog Header • Custom Background • Social Media Icons • Custom Sidebar Title Design • About Me Image & Text Caption Design

```html
<!DOCTYPE html>
<html lang="en">
<head>
<meta charset="utf-8">
<title>Coral Dunes Luxury Weddings</title>
<link rel="stylesheet" href="https://fonts.googleapis.com/css2?family=Raleway:wght@400;500&family=Roboto:wght@400&family=Dancing+Script:wght@400&display=swap">
<style>
  :root {
    --white: #ffffff;
    --gold: #c9a23c;
    --blush: #f9e1e4;
    --blush-button: #f5d2d6;
    --blush-deep: #f0b9c3;
    --cream: #f1ecd3;
    --cream-light: #fbf9ef;
    --nav-text: #a6a6a6;
    --label-text: #a3a08c;
    --footer-text: #9c9a88;
  }
  * { box-sizing: border-box; margin: 0; padding: 0; }
  html, body { width: 1200px; height: 1189px; overflow: hidden; background: var(--white); }
  .page { position: relative; width: 1200px; height: 1189px; font-family: "Raleway", sans-serif; }

  .brand {
    position: absolute; top: 0; left: 0; width: 1200px; height: 188px;
    display: flex; flex-direction: column; align-items: center; justify-content: center; gap: 14px;
  }
  .brand-emblem {
    width: 44px; height: 44px; border-radius: 50%; background: var(--blush-deep);
  }
  .brand-name {
    font-family: "Raleway", sans-serif; font-weight: 500; font-size: 40px;
    letter-spacing: 3px; color: var(--gold); line-height: 1;
  }

  .main-nav {
    position: absolute; top: 188px; left: 0; width: 1200px; height: 54px;
    background: var(--blush);
  }
  .main-nav a {
    position: absolute; top: 0; line-height: 54px; transform: translateX(-50%);
    font-family: "Roboto", sans-serif; font-size: 19px; color: var(--nav-text);
    text-decoration: none;
  }

  .content {
    position: absolute; top: 247px; left: 0; width: 1200px; height: 780px;
    background: var(--cream-light);
  }
  .hero {
    position: absolute; top: 21px; left: 117px; width: 990px; height: 432px;
    background: linear-gradient(180deg, #e9eef0 0%, #dfe8ea 40%, #3fa3ad 62%, #1d7f8e 78%, #5f6d62 88%, #2f4b53 100%);
  }

  .feature-card {
    position: absolute; top: 498px; width: 306px; height: 230px;
    background: var(--cream);
  }
  .feature-card::before {
    content: ""; position: absolute; inset: 6px; border: 2px solid var(--white);
  }
  .feature-photo { position: absolute; top: 20px; left: 23px; width: 258px; height: 112px; }
  .feature-title {
    position: absolute; top: 143px; left: 0; width: 100%; text-align: center;
    font-size: 17px; font-weight: 400; letter-spacing: 3px; color: var(--label-text);
  }
  .read-more {
    position: absolute; display: block; width: 137px; height: 36px;
    background: var(--blush-button); color: var(--white); text-align: center;
    font-family: "Dancing Script", cursive; font-size: 21px; line-height: 36px;
    text-decoration: none;
  }
  .feature-card .read-more { top: 170px; left: 84px; }

  .site-footer {
    position: absolute; top: 1027px; left: 0; width: 1200px; height: 162px;
    background: var(--cream); border-top: 4px solid var(--white);
  }
  .footer-mark {
    position: absolute; top: 20px; left: 115px; width: 112px; height: 108px;
    border: 3px solid var(--gold); display: flex; flex-direction: column;
    align-items: center; justify-content: center; gap: 6px;
    text-align: center; padding: 8px;
    font-size: 13px; line-height: 1.25; color: var(--gold); font-weight: 500;
  }
  .footer-mark-dot { width: 18px; height: 18px; border-radius: 50%; background: var(--blush-deep); }
  .footer-heading {
    position: absolute; top: 19px; font-size: 17px; font-weight: 400; letter-spacing: 3px; color: var(--footer-text);
  }
  .email-field {
    position: absolute; top: 45px; left: 253px; width: 302px; height: 33px;
    background: var(--white); border: none; padding-left: 14px;
    font-family: "Raleway", sans-serif; font-size: 12px; letter-spacing: 1.5px; color: var(--footer-text);
  }
  .site-footer .read-more { top: 93px; left: 253px; width: 138px; height: 35px; line-height: 35px; }
  .social-links { position: absolute; top: 58px; left: 693px; }
</style>
</head>
<body>
<div class="page">
  <header class="brand">
    <span class="brand-emblem" aria-hidden="true"></span>
    <span class="brand-name">Coral Dunes Luxury Weddings</span>
  </header>

  <nav class="main-nav">
    <a href="#" style="left:269px">WELCOME</a>
    <a href="#" style="left:407px">VENUES</a>
    <a href="#" style="left:552px">GALLERIES</a>
    <a href="#" style="left:685px">BLOG</a>
    <a href="#" style="left:815px">CONTACT</a>
    <a href="#" style="left:955px">ESPAÑOL</a>
  </nav>

  <main class="content" role="img" aria-label="Soft cream background with faint line-drawn roses">
    <div class="hero" role="img" aria-label="Wedding couple by an infinity pool under palm trees with paper lanterns and the turquoise sea behind"></div>

    <section class="feature-card" style="left:121px">
      <div class="feature-photo" role="img" aria-label="Couple in a green jungle setting" style="background:linear-gradient(135deg,#3d4a22,#7b8a4a 55%,#2b3418)"></div>
      <h2 class="feature-title">OUR SERVICES</h2>
      <a class="read-more" href="#">read more</a>
    </section>

    <section class="feature-card" style="left:457px">
      <div class="feature-photo" role="img" aria-label="Bride and groom walking along a white sand beach" style="background:linear-gradient(90deg,#8fb0b4,#dcdad0 45%,#e9e5dc 70%,#4f7a4a)"></div>
      <h2 class="feature-title">PHOTO GALLERY</h2>
      <a class="read-more" href="#">read more</a>
    </section>

    <section class="feature-card" style="left:799px">
      <div class="feature-photo" role="img" aria-label="Bridal bouquet of pink roses and peonies" style="background:linear-gradient(135deg,#e58aa0,#f4b8a8 45%,#f3d7cf 70%,#d9698a)"></div>
      <h2 class="feature-title">BLOG</h2>
      <a class="read-more" href="#">read more</a>
    </section>
  </main>

  <footer class="site-footer">
    <div class="footer-mark">
      <span class="footer-mark-dot" aria-hidden="true"></span>
      <span>Coral Dunes Luxury Weddings</span>
    </div>
    <p class="footer-heading" style="left:252px">SUBSCRIBE TO STAY INFORM!</p>
    <input class="email-field" type="text" placeholder="email" aria-label="email">
    <a class="read-more" href="#">read more</a>
    <p class="footer-heading" style="left:667px">LET'S BE SOCIAL!</p>
    <svg class="social-links" width="372" height="52" viewBox="0 0 372 52" role="img" aria-label="Social media links">
      <g fill="#ffffff">
        <circle cx="24" cy="26" r="24"/>
        <circle cx="84" cy="26" r="24"/>
        <circle cx="144" cy="26" r="24"/>
        <circle cx="203" cy="26" r="24"/>
        <circle cx="263" cy="26" r="24"/>
        <circle cx="323" cy="26" r="24"/>
      </g>
      <g fill="#f0b9c3">
        <circle cx="24" cy="26" r="7"/>
        <circle cx="84" cy="26" r="7"/>
        <circle cx="144" cy="26" r="7"/>
        <circle cx="203" cy="26" r="7"/>
        <circle cx="263" cy="26" r="7"/>
        <circle cx="323" cy="26" r="7"/>
      </g>
    </svg>
  </footer>
</div>
</body>
</html>
```